Progressive/contemporary business card design for successful Startups as a Service Company

New logo launched in 2020. New website launched in 2021. Now that COVID is (mostly) behind us, I'm networking with more people and need a business card that matches the company/logo design aesthetic.

```html
<!DOCTYPE html>
<html lang="en">
<head>
<meta charset="utf-8">
<title>Buildways Business Card</title>
<link rel="stylesheet" href="https://fonts.googleapis.com/css2?family=Open+Sans:wght@400;700&family=Raleway:wght@500&display=swap">
<style>
  :root {
    --backdrop: #d9d9d7;
    --card-white: #ffffff;
    --ink-slate: #3a4459;
    --ink-grey: #5b5f66;
    --accent-blue: #1e88d6;
    --rule-blue: #4aa3e0;
    --navy-light: #5a6886;
    --navy-dark: #3b465f;
    --mark-light: #e6ebf3;
    --icon-pink: #d6287c;
    --icon-green: #3fae3a;
    --icon-red: #e0312f;
  }
  html, body {
    margin: 0;
    width: 1200px;
    height: 801px;
    overflow: hidden;
    background: var(--backdrop);
  }
  .stage {
    position: relative;
    width: 1200px;
    height: 801px;
  }
  .card {
    position: absolute;
    width: 525px;
    height: 300px;
    box-shadow: 0 4px 14px rgba(0,0,0,0.14);
  }
  .card-front {
    left: 50px;
    top: 110px;
    background: var(--card-white);
  }
  .card-back {
    right: 50px;
    top: 391px;
    overflow: hidden;
  }

  /* Front */
  .wordmark {
    position: absolute;
    left: 34px;
    top: 184px;
    display: flex;
    align-items: center;
    gap: 10px;
    font-family: "Raleway", sans-serif;
    font-weight: 500;
    font-size: 24px;
    line-height: 30px;
    letter-spacing: 5px;
    color: var(--ink-slate);
  }
  .wordmark-square {
    width: 18px;
    height: 18px;
    background: var(--ink-slate);
  }
  .contact-block {
    position: absolute;
    left: 300px;
    top: 58px;
    padding-left: 16px;
    border-left: 1.5px solid var(--rule-blue);
    font-family: "Open Sans", sans-serif;
    color: var(--ink-grey);
    font-size: 12.5px;
    line-height: 19px;
  }
  .person-name {
    margin: 0;
    font-weight: 700;
    font-size: 19px;
    line-height: 24px;
    color: var(--accent-blue);
    letter-spacing: 0.3px;
  }
  .person-title, .address-line { margin: 0; }
  .address { margin: 4px 0 8px; }
  .contact-list {
    list-style: none;
    margin: 0;
    padding: 0;
  }
  .contact-list li {
    display: flex;
    align-items: center;
    gap: 6px;
    white-space: nowrap;
  }
  .contact-icon { width: 10px; height: 10px; flex: none; }

  /* Back */
  .pattern-fill {
    position: absolute;
    inset: 0;
    background: linear-gradient(135deg, var(--navy-dark) 0%, var(--navy-light) 100%);
  }
  .back-wordmark {
    position: absolute;
    right: 40px;
    bottom: 118px;
    font-family: "Raleway", sans-serif;
    font-weight: 500;
    font-size: 22px;
    letter-spacing: 5px;
    color: var(--mark-light);
  }
</style>
</head>
<body>
<main class="stage">
  <section class="card card-front" aria-label="Card front">
    <div class="wordmark">
      <span class="wordmark-text">BUILDWAYS</span>
      <span class="wordmark-square"></span>
    </div>
    <div class="contact-block">
      <h1 class="person-name">DANIEL HARROW</h1>
      <p class="person-title">President</p>
      <div class="address">
        <p class="address-line">418 N Harlow Ave., Suite B</p>
        <p class="address-line">Brookfield, IL 60513</p>
      </div>
      <ul class="contact-list">
        <li>
          <svg class="contact-icon" viewBox="0 0 10 10" aria-hidden="true">
            <path d="M2 1 L4 1 L4.6 3 L3.4 3.8 Q4.5 6 6.2 6.6 L7 5.4 L9 6 L9 8 Q5 9 2.2 5 Q1 3 2 1 Z" fill="var(--icon-pink)"/>
          </svg>
          <span>(555) 014-2273</span>
        </li>
        <li>
          <svg class="contact-icon" viewBox="0 0 10 10" aria-hidden="true">
            <rect x="0.5" y="2" width="9" height="6.5" fill="var(--icon-green)"/>
            <path d="M0.5 2 L5 5.6 L9.5 2" fill="none" stroke="#fff" stroke-width="0.9"/>
          </svg>
          <span>hello@buildwaysconsulting.com</span>
        </li>
        <li>
          <svg class="contact-icon" viewBox="0 0 10 10" aria-hidden="true">
            <circle cx="5" cy="5" r="4.5" fill="var(--icon-red)"/>
            <path d="M0.5 5 H9.5 M5 0.5 Q2.5 5 5 9.5 M5 0.5 Q7.5 5 5 9.5" fill="none" stroke="#fff" stroke-width="0.7"/>
          </svg>
          <span>www.buildways.solutions</span>
        </li>
      </ul>
    </div>
  </section>

  <section class="card card-back" aria-label="Card back">
    <div class="pattern-fill" role="img" aria-label="Embossed navy lattice pattern of interlocking triangles"></div>
    <div class="back-wordmark">BUILDWAYS</div>
  </section>
</main>
</body>
</html>
```